Value-added components of an energy-as-a-service provider

FolwenTide (www.folwentide.example) is a turnkey energy solutions provider for educational institutions—which essentially means we can make recommendations for ways to improve heating, cooling, ventilation, lighting, building controls, etc., and then turn around and project-manage the implementation of these recommendations.Part of what makes us different than our competitors is recognizing the unique way that educational institutions make decisions: they employ a more collaborative approach, and given the 24/7 nature of school operations, any construction needs to be very carefully planned and communicated with building occupants.We are looking at competing in the "energy-as-a-service" (EaaS) field, which effectively capitalizes on the way institutions can self-supply energy. The biggest hurdles for most projects that either produce or conserve energy are (1) upfront cost (these projects are really expensive) and (2) implementation (full-time employees on campuses already have too much on their plates). What EaaS providers can do is alleviate these burdens by finding the capital to pay for equipment, which the school then repays through the associated energy savings. Providers also do the work of implementing the changes.FolwenTide offers the same basic characteristics that other EaaS providers offer—but we have a few elements that are like the icing on the cake, or the cherry on top (insert your own dessert metaphor here). Namely, we work exclusively with schools and are familiar with that environment, know how to work around sensitive scheduling constraints, know how to engage stakeholders in an academic environment, etc. That's what we would like help with in a graphic. There's a couple of renderings we did in-house, but the feedback on the less crude one attached is that there's a bit too much emphasis on the three differentiating elements, and that it could be a bit more visually appealing. We're really open to suggestions here, but keeping it simple and classy is still paramount. Attached is the FolwenTide brand standards guidebook, which has our color palette and fonts and such, and a couple of iterations of our logo are also attached.
Look and feel
Each slider illustrates characteristics of the customer's brand and the style your logo design should communicate.

```html
<!DOCTYPE html>
<html lang="en">
<head>
<meta charset="utf-8">
<title>FolwenTide Difference</title>
<link rel="stylesheet" href="https://fonts.googleapis.com/css2?family=Open+Sans:wght@600;700;800&display=swap">
<style>
  :root {
    --leaf: #7cc243;
    --leaf-deep: #5aad36;
    --leaf-light: #c4e48a;
    --navy: #1d3a6a;
    --plug: #2ba6df;
    --slate: #4f7585;
    --ink-grey: #7b7b7b;
    --paper: #ffffff;
  }
  * { box-sizing: border-box; margin: 0; padding: 0; }
  html, body { width: 1200px; height: 848px; overflow: hidden; background: var(--paper); }
  body { font-family: "Open Sans", Arial, sans-serif; }
  .poster { position: relative; width: 1200px; height: 848px; background: var(--paper); }
  .art { position: absolute; inset: 0; }
  .txt { position: absolute; font-weight: 700; text-transform: uppercase; white-space: nowrap; }

  .brand { left: 0; width: 1200px; top: 32px; text-align: center; color: var(--ink-grey);
           font-size: 28px; font-weight: 600; letter-spacing: 1px; }
  .brand-square { display: inline-block; width: 22px; height: 22px; background: var(--leaf);
                  margin-left: 10px; vertical-align: -2px; }

  .banner { left: 352px; top: 100px; width: 496px; height: 54px; background: var(--leaf);
            color: var(--navy); font-size: 34px; font-weight: 800; text-align: center; line-height: 54px; }
  .tagline { left: 0; width: 1200px; top: 178px; text-align: center; color: var(--leaf-deep); font-size: 23px; }

  .column-title { color: var(--navy); font-size: 19px; top: 254px; }
  .column-title.ours { left: 128px; }
  .column-title.theirs { right: 86px; }

  .service { color: var(--leaf-deep); font-size: 14px; line-height: 16px; }
  .service.right-aligned { text-align: right; }

  .institution-label { left: 580px; width: 220px; top: 572px; text-align: center; color: var(--slate); font-size: 13px; }

  .team-name { color: #fff; font-size: 26px; top: 724px; text-align: center; }
  .team-name.ours { left: 180px; width: 346px; font-weight: 600; letter-spacing: 1px; }
  .team-name.theirs { left: 683px; width: 304px; font-size: 23px; }
  .versus { left: 565px; top: 712px; width: 80px; text-align: center; color: var(--navy); font-size: 44px; font-weight: 800; }
</style>
</head>
<body>
<main class="poster">
  <svg class="art" width="1200" height="848" viewBox="0 0 1200 848">
    <defs>
      <linearGradient id="team-art" x1="0" y1="0" x2="0" y2="1">
        <stop offset="0" stop-color="#8a8a8a"/>
        <stop offset="0.45" stop-color="#6fb843"/>
        <stop offset="1" stop-color="#c4e48a"/>
      </linearGradient>
      <linearGradient id="campus" x1="0" y1="0" x2="0" y2="1">
        <stop offset="0" stop-color="#6d8f9d"/>
        <stop offset="1" stop-color="#4f7585"/>
      </linearGradient>
      <symbol id="plug-icon" viewBox="0 0 28 22">
        <rect x="0" y="9" width="6" height="4" fill="var(--plug)"/>
        <rect x="5" y="2" width="16" height="18" rx="3" fill="var(--plug)"/>
        <rect x="21" y="5" width="7" height="3" fill="var(--plug)"/>
        <rect x="21" y="14" width="7" height="3" fill="var(--plug)"/>
      </symbol>
    </defs>

    <g class="cable" fill="none" stroke="var(--leaf)" stroke-width="5" stroke-linecap="round">
      <path d="M96 517 L96 330 Q96 304 122 304 L326 304 Q352 304 352 330 L352 500 Q352 517 335 517 L96 517"/>
      <path d="M96 517 C96 590 110 660 182 690"/>
      <path d="M96 368 H150"/><path d="M96 412 H150"/><path d="M96 452 H150"/><path d="M96 496 H150"/>
      <path d="M352 376 H392"/><path d="M352 430 H392"/><path d="M352 484 H392"/>
    </g>
    <g class="cable" fill="none" stroke="var(--leaf)" stroke-width="5" stroke-linecap="round">
      <path d="M1110 300 Q1160 310 1160 380 L1160 600 C1160 660 1080 700 988 700"/>
      <path d="M1068 360 H1160"/><path d="M1068 404 H1160"/><path d="M1068 448 H1160"/><path d="M1068 492 H1160"/>
    </g>

    <g class="plugs">
      <use href="#plug-icon" x="148" y="357" width="30" height="24"/>
      <use href="#plug-icon" x="148" y="401" width="30" height="24"/>
      <use href="#plug-icon" x="148" y="441" width="30" height="24"/>
      <use href="#plug-icon" x="148" y="485" width="30" height="24"/>
      <use href="#plug-icon" x="390" y="365" width="30" height="24"/>
      <use href="#plug-icon" x="390" y="419" width="30" height="24"/>
      <use href="#plug-icon" x="390" y="473" width="30" height="24"/>
      <g transform="translate(2140 0) scale(-1 1)">
        <use href="#plug-icon" x="1040" y="349" width="30" height="24"/>
        <use href="#plug-icon" x="1040" y="393" width="30" height="24"/>
        <use href="#plug-icon" x="1040" y="437" width="30" height="24"/>
        <use href="#plug-icon" x="1040" y="481" width="30" height="24"/>
      </g>
    </g>

    <rect class="institution" x="560" y="300" width="240" height="260" rx="6" fill="url(#campus)"
          role="img" aria-label="Illustration of a school building with solar panels, clouds and sun, and an adult walking with a child"/>

    <rect class="team-art ours" x="180" y="590" width="346" height="225" rx="60" fill="url(#team-art)"
          role="img" aria-label="Illustration of a green hand holding up a large team of people"/>
    <rect class="team-art theirs" x="683" y="632" width="304" height="183" rx="55" fill="url(#team-art)"
          role="img" aria-label="Illustration of a green hand holding up a smaller team of people"/>
  </svg>

  <div class="txt brand">FolwenTide<span class="brand-square"></span></div>
  <div class="txt banner">FolwenTide Difference</div>
  <div class="txt tagline">Energy Solutions Provider for Educational Institutions</div>

  <div class="txt column-title ours">FolwenTide Services</div>
  <div class="txt column-title theirs">Competitor’s Services</div>

  <div class="txt service" style="left:188px;top:361px">Financing</div>
  <div class="txt service" style="left:188px;top:405px">Engineering</div>
  <div class="txt service" style="left:188px;top:445px">Construction</div>
  <div class="txt service" style="left:188px;top:489px">O&amp;M</div>
  <div class="txt service" style="left:430px;top:361px">Stakeholder<br>Engagement</div>
  <div class="txt service" style="left:430px;top:415px">Academic<br>Integration</div>
  <div class="txt service" style="left:430px;top:469px">Scheduling<br>Sensitivity</div>

  <div class="txt service right-aligned" style="right:168px;top:353px">Financing</div>
  <div class="txt service right-aligned" style="right:168px;top:397px">Engineering</div>
  <div class="txt service right-aligned" style="right:168px;top:441px">Construction</div>
  <div class="txt service right-aligned" style="right:168px;top:485px">O&amp;M</div>

  <div class="txt institution-label">Educational Institution</div>

  <div class="txt team-name ours">FolwenTide</div>
  <div class="txt versus">VS</div>
  <div class="txt team-name theirs">Competitor</div>
</main>
</body>
</html>
```